Medical Practice Business Card

we need a business card for our new medical ophthalmology practice based in Needham Massachusetts. we are looking for a simple , modern and elegant design.
the card needs to contain the following
1- the logo of our practice (please see attached file)
2- the name of the practice : "Silver Birch Retina Care"
3- Doctor's Name: Tobias Rendell MD PhD
4- Specialty: Board-Certified Vitreoretinal Surgeon
5- practice address: 87 Larkspur Ave, Suite 210, Alderbrook VT 05482
7- Office number: 802- 482 - 7730
8- fax number: 802- 391 - 2268
9- email: info@sbretinahub.example
10- website: www.sbretinahub.example

```html
<!DOCTYPE html>
<html lang="en">
<head>
<meta charset="utf-8">
<title>Silver Birch Retina Care – Business Card</title>
<link href="https://fonts.googleapis.com/css2?family=Tinos:wght@400;700&display=swap" rel="stylesheet">
<style>
  :root {
    --backdrop: #232323;
    --front-deep: #0d3a66;
    --front-bright: #0a55a6;
    --back-card: #1f1f24;
    --brand-front: #2a78d0;
    --brand-faint: #173e70;
    --accent-sky: #5fb8e0;
    --accent-blue: #1d5fb0;
    --icon-blue: #4a9fd8;
    --band-light: #86d4e6;
    --band-dark: #0f55b0;
    --ink-light: #f2f4f7;
    --rule: #9aa0a8;
  }
  * { box-sizing: border-box; margin: 0; padding: 0; }
  html, body { width: 1200px; height: 780px; overflow: hidden; }
  body {
    background: var(--backdrop);
    font-family: "Tinos", "Times New Roman", serif;
    display: flex;
    align-items: center;
    justify-content: center;
    gap: 30px;
  }
  .card {
    width: 560px;
    height: 320px;
    position: relative;
    overflow: hidden;
    box-shadow: 0 14px 30px rgba(0,0,0,.55);
  }

  /* Front */
  .card-front {
    background: linear-gradient(200deg, var(--front-deep) 0%, var(--front-bright) 100%);
    display: flex;
    align-items: center;
    justify-content: center;
    gap: 18px;
  }
  .brand-dot { border-radius: 50%; flex: none; }
  .brand-name {
    font-weight: 700;
    text-transform: uppercase;
    letter-spacing: 1px;
    line-height: 1.05;
  }
  .card-front .brand-name { font-size: 34px; color: var(--brand-front); }
  .card-front .brand-dot { width: 22px; height: 22px; background: var(--brand-front); }

  /* Back */
  .card-back { background: var(--back-card); }
  .brand-block {
    position: absolute;
    left: 34px; top: 96px;
    width: 215px;
    display: flex; align-items: center; gap: 12px;
  }
  .card-back .brand-name { font-size: 21px; color: var(--brand-faint); }
  .card-back .brand-dot { width: 16px; height: 16px; background: var(--brand-faint); }

  .divider {
    position: absolute;
    left: 262px; top: 34px;
    width: 1px; height: 190px;
    background: var(--rule);
  }
  .details {
    position: absolute;
    left: 284px; top: 42px;
    right: 16px;
    color: var(--ink-light);
  }
  .doctor-name {
    font-size: 17px;
    font-weight: 700;
    color: var(--accent-sky);
    text-transform: uppercase;
    white-space: nowrap;
  }
  .doctor-name .credentials { color: var(--accent-blue); }
  .specialty { font-size: 13px; margin-top: 3px; white-space: nowrap; }
  .contact-list { list-style: none; margin-top: 22px; }
  .contact-list li {
    display: flex; align-items: center; gap: 9px;
    font-size: 14px; line-height: 1.6;
    white-space: nowrap;
  }
  .contact-list svg { width: 13px; height: 13px; flex: none; }

  .address-band {
    position: absolute;
    left: 0; right: 0; bottom: 32px;
    height: 30px;
    background: linear-gradient(90deg, var(--band-light), var(--band-dark));
    display: flex; align-items: center;
    padding-left: 130px;
    color: var(--ink-light);
    font-size: 14.5px;
    white-space: nowrap;
  }
  .band-mark {
    position: absolute;
    right: 34px; top: 50%;
    width: 34px; height: 34px;
    margin-top: -17px;
    border-radius: 50%;
    border: 3px solid var(--band-dark);
    background: var(--back-card);
  }
</style>
</head>
<body>

  <section class="card card-front" aria-label="Card front">
    <span class="brand-dot"></span>
    <span class="brand-name">Silver Birch<br>Retina Care</span>
  </section>

  <section class="card card-back" aria-label="Card back">
    <div class="brand-block">
      <span class="brand-dot"></span>
      <span class="brand-name">Silver Birch<br>Retina Care</span>
    </div>

    <div class="divider"></div>

    <div class="details">
      <p class="doctor-name">Tobias Rendell <span class="credentials">MD PhD</span></p>
      <p class="specialty">Board-Certified Vitreoretinal Surgeon</p>
      <ul class="contact-list">
        <li>
          <svg viewBox="0 0 16 16" aria-hidden="true"><path fill="#4a9fd8" d="M3.6 1.5l2.3 2.7-1.3 1.8c.9 1.9 2.5 3.5 4.4 4.4l1.8-1.3 2.7 2.3-1.4 2.2C7 13.4 2.6 9 1.4 2.9z"/></svg>
          802- 482 - 7730
        </li>
        <li>
          <svg viewBox="0 0 16 16" aria-hidden="true"><path fill="#4a9fd8" d="M4 1h6l2 2v4h2v8H2V7h2zm1 1v5h6V3.5L9.5 2zM4 9v1h2V9zm3 0v1h2V9zm3 0v1h2V9zM4 11v1h2v-1zm3 0v1h2v-1zm3 0v1h2v-1z"/></svg>
          802- 391 - 2268
        </li>
        <li>
          <svg viewBox="0 0 16 16" aria-hidden="true"><path fill="#4a9fd8" d="M1 4h14v9H1zm1.2 1L8 9.2 13.8 5zM2 6.2V12h12V6.2L8 10.5z"/></svg>
          info@sbretinahub.example
        </li>
        <li>
          <svg viewBox="0 0 16 16" aria-hidden="true"><circle cx="8" cy="8" r="6.5" fill="none" stroke="#4a9fd8" stroke-width="1.5"/><path d="M1.5 8h13M8 1.5c-3 3.5-3 9.5 0 13M8 1.5c3 3.5 3 9.5 0 13" fill="none" stroke="#4a9fd8" stroke-width="1.2"/></svg>
          www.sbretinahub.example
        </li>
      </ul>
    </div>

    <div class="address-band">
      87 Larkspur Ave, Suite 210, Alderbrook VT 05482
      <span class="band-mark"></span>
    </div>
  </section>

</body>
</html>
```